Flyer für Anbieter einer Fortbildung für Beratungslehrer
Zielgruppe
Wir bieten eine Fortbildung für Beratungslehrer an, welche mit immer komplexer werdenden psychischen Fällen arbeiten. Diese Fortbildung setzt sich gezielt mit der Stärkung des Selbstkonzepts, der Resilienz sowie dem Selbstwert auseinander. Wir stellen dabei die Anliegen der Klienten in den Fokus.
Das Angebot basiert auf dem Konzept des Lernfeld Zuversicht des Kurt- Wendland-Institut, Heidelberg
Aufgabenstellung
Die Inhalte der Fortbildung sollen enthalten sein.
Layout sollte unseren Arbeitsbereich im psychologischen Wohlbefinden widerspiegeln

```html
<!DOCTYPE html>
<html lang="de">
<head>
<meta charset="utf-8">
<title>Fortbildung für Beratungslehrer – Flyer</title>
<link href="https://fonts.googleapis.com/css2?family=Montserrat:wght@400;500;600;700;800&display=swap" rel="stylesheet">
<style>
  :root {
    --teal: #5fa596;
    --ink: #3a3a3a;
    --white: #ffffff;
    --paper: #fbfbfb;
    --panel: #f0f1f1;
    --backdrop: #e7e9e8;
  }
  * { margin: 0; padding: 0; box-sizing: border-box; }
  html, body { width: 1200px; height: 589px; overflow: hidden; }
  body {
    background: var(--backdrop);
    font-family: "Montserrat", sans-serif;
    color: var(--ink);
  }
  .flyer {
    position: absolute;
    left: 392px; top: 0;
    width: 416px; height: 589px;
    background: var(--paper);
    overflow: hidden;
  }
  .header {
    position: absolute; left: 0; top: 0;
    width: 246px; height: 154px;
    background: var(--teal);
    color: var(--white);
    padding: 18px 20px 0 20px;
  }
  .header h1 {
    font-weight: 800; font-size: 15.4px; line-height: 18.8px;
    text-transform: uppercase; letter-spacing: 0.2px;
  }
  .header .kicker { font-weight: 700; font-size: 9.2px; margin-top: 10px; }
  .header .sub { font-weight: 400; font-size: 8.6px; line-height: 11px; margin-top: 2px; }
  .photo {
    position: absolute; left: 246px; top: 0;
    width: 170px; height: 202px;
    background: linear-gradient(135deg, #4c6f93 0%, #c9b79a 45%, #d8c3a0 70%, #efe9e1 100%);
  }
  .content {
    position: absolute; left: 20px; top: 169px; width: 204px;
    font-size: 6.9px; line-height: 8.9px;
  }
  .content p { text-align: justify; }
  .content h2 {
    color: var(--teal); font-weight: 700; font-size: 11.6px; line-height: 12.6px;
    text-transform: uppercase; letter-spacing: 0.2px;
    margin: 12px 0 6px;
  }
  .content h3 {
    color: var(--teal); font-weight: 500; font-size: 9.3px;
    margin: 10px 0 4px;
  }
  .content h2 + h3 { margin-top: 2px; }
  .content .closing {
    color: var(--teal); font-weight: 500; font-size: 9.4px; line-height: 10.6px;
    margin-top: 12px; text-align: left;
  }
  .audience {
    position: absolute; left: 265px; top: 230px;
    width: 160px; height: 149px;
    background: var(--panel);
    border-radius: 18px 0 0 18px;
    padding: 17px 16px 0 17px;
  }
  .audience h2 {
    font-weight: 500; font-size: 10.2px; line-height: 14px;
    text-transform: uppercase; margin-bottom: 6px;
  }
  .audience p { font-size: 6.7px; line-height: 8.9px; text-align: justify; width: 95px; }
  .contact {
    position: absolute; left: 246px; top: 401px;
    width: 170px; height: 188px;
    background: var(--teal);
    color: var(--white);
    padding: 0 18px;
  }
  .brand-name {
    display: block;
    margin-top: 38px; height: 30px;
    font-weight: 500; font-size: 17px; letter-spacing: 1.5px;
    text-transform: uppercase; text-align: center;
  }
  .contact h2 {
    font-weight: 800; font-size: 12px; line-height: 13px;
    text-transform: uppercase; margin-top: 42px;
  }
  .contact p {
    font-size: 6.7px; line-height: 8.9px; margin-top: 6px; text-align: justify;
  }
</style>
</head>
<body>
<article class="flyer">
  <header class="header">
    <h1>Stärkung des Selbstkonzepts, des Selbstwerts und der Resilienz</h1>
    <p class="kicker">Fortbildung für Beratungslehrer</p>
    <p class="sub">Stärkung des Selbstkonzepts,<br>des Selbstwerts und der Resilienz</p>
  </header>

  <div class="photo" role="img" aria-label="Foto: Beratungsgespräch, eine Person macht Notizen auf einem Block, die andere sitzt mit gefalteten Händen gegenüber"></div>

  <section class="content">
    <p>Sie sind Beratungslehrer und möchten Ihre Klient*innen bestmöglich in ihrer persönlichen Entwicklung unterstützen? Dann ist diese Fortbildung genau das Richtige für Sie!</p>

    <h2>Inhalt der Fortbildung</h2>
    <p>In dieser praxisorientierten Fortbildung lernen Sie, wie Sie Ihre Klient*innen gezielt in den Bereichen Selbstkonzept, Selbstwert und Resilienz stärken können. Basierend auf dem bewährten Konzept des Lernfelds Zuversicht werden Ihnen Methoden und Techniken vermittelt, die direkt in der Beratung anwendbar sind.</p>

    <h2>Was erwartet Sie?</h2>
    <h3>1. Stärkung des Selbstkonzepts:</h3>
    <p>Erfahren Sie, wie Sie Klient*innen helfen können, ein gesundes und positives Selbstbild zu entwickeln.</p>
    <h3>2. Aufbau von Selbstwert:</h3>
    <p>Entdecken Sie Wege, um das Selbstvertrauen und die Eigenmotivation Ihrer Klient*innen nachhaltig zu fördern.</p>
    <h3>3. Förderung der Resilienz</h3>
    <p>Lernen Sie Strategien kennen, mit denen Klient*innen Krisen und Herausforderungen besser bewältigen können.</p>

    <h2>Warum das<br>Lernfeld Zuversicht?</h2>
    <p>Das Lernfeld Zuversicht verbindet positive Psychologie mit pädagogischen Ansätzen und ermöglicht eine ganzheitliche Förderung der Persönlichkeit. Ziel ist es, Klient*innen auf ein erfülltes und zufriedenes Leben vorzubereiten.</p>

    <p class="closing">Investieren Sie in die Zukunft Ihrer Klient*innen – und in Ihre eigene Weiterbildung!</p>
  </section>

  <aside class="audience">
    <h2>Für wen ist die Fortbildung geeignet?</h2>
    <p>Diese Fortbildung richtet sich an Beratungslehrer, Schulpsychologen und pädagogische Fachkräfte, die ihre Kompetenzen erweitern und ihre Klient*innen bestmöglich unterstützen möchten.</p>
  </aside>

  <footer class="contact">
    <span class="brand-name">Mutwerk</span>
    <h2>Termine &amp;<br>Anmeldung</h2>
    <p>Lorem ipsum dolor sit amet, consectetur adipiscing elit. Pellentesque vitae maximus sapien.</p>
  </footer>
</article>
</body>
</html>
```